SnapMingle App Log-in Screen Design

We need a design for the main Log-in screen of an App we are developing.

The only requirement is it must have for 2 buttons called 'play' and 'register'. The rest of the screen design is up to you.

We want it to be fun and engaging and we have no preference between an animation/cartoon look or a classical photo background. Essentially we don't have a preconceived idea so no point asking us for direction... Each design will be judged on its wow factor.

Without giving too much away the core concept of the App is that guests at events can Log-in to the event through the App and take photos on their phones and these photos will be made available to the event organisers.
Updates

Designs that are jut plain screen with buttons will not be considered.  We are looking for something that engages the user... get creative!

```html
<!DOCTYPE html>
<html lang="en">
<head>
<meta charset="utf-8">
<title>SnapMingle – Log in</title>
<link rel="stylesheet" href="https://fonts.googleapis.com/css2?family=Roboto:wght@300;400&display=swap">
<style>
  :root {
    --bg-light: #adbd33;
    --bg-mid: #6d8a1a;
    --bg-dark: #4f6a0a;
    --card-top: #ffffff;
    --card-bottom: #fde3d0;
    --card-edge-light: #e3c2a6;
    --card-edge: #a35a33;
    --field: #ffffff;
    --field-line: #f1d9d0;
    --field-text: #5a1a0c;
    --play-top: #1c6aa6;
    --play-bottom: #0c3f72;
    --play-stroke: #0a2f55;
    --register-top: #d8141a;
    --register-bottom: #a70a10;
    --register-stroke: #7d070b;
    --button-text: #ffffff;
    --button-shadow: #3e5210;
  }
  html, body {
    margin: 0;
    padding: 0;
    overflow: hidden;
  }
  .screen {
    position: relative;
    width: 1200px;
    height: 683px;
    overflow: hidden;
    background: radial-gradient(ellipse 640px 560px at 576px 132px, var(--bg-light) 0%, var(--bg-mid) 55%, var(--bg-dark) 100%);
    font-family: "Roboto", "Helvetica Neue", Arial, sans-serif;
  }
  .login-shape {
    position: absolute;
    left: 0;
    top: 0;
  }
  .field {
    position: absolute;
    left: 379px;
    width: 410px;
    height: 47px;
    margin: 0;
    background: var(--field);
    border-top: 2px solid var(--field-line);
    box-sizing: border-box;
    color: var(--field-text);
    font-weight: 400;
    line-height: 45px;
    padding-left: 19px;
  }
  .field-user {
    top: 242px;
    font-size: 18px;
  }
  .field-password {
    top: 309px;
    font-size: 14px;
    letter-spacing: 0.6px;
  }
  .button-label {
    position: absolute;
    top: 427px;
    height: 36px;
    margin: 0;
    line-height: 36px;
    text-align: center;
    color: var(--button-text);
    font-size: 23px;
    font-weight: 300;
  }
  .button-label-play { left: 481px; width: 150px; }
  .button-label-register { left: 639px; width: 152px; }
</style>
</head>
<body>
<main class="screen">
  <svg class="login-shape" width="1200" height="683" viewBox="0 0 1200 683" aria-hidden="true">
    <defs>
      <linearGradient id="card-fill" x1="0" y1="0" x2="0" y2="1">
        <stop offset="0" stop-color="var(--card-top)"/>
        <stop offset="1" stop-color="var(--card-bottom)"/>
      </linearGradient>
      <linearGradient id="card-edge-fill" x1="0" y1="0" x2="1" y2="1">
        <stop offset="0" stop-color="var(--card-edge-light)"/>
        <stop offset="1" stop-color="var(--card-edge)"/>
      </linearGradient>
      <linearGradient id="play-fill" x1="0" y1="0" x2="0" y2="1">
        <stop offset="0" stop-color="var(--play-top)"/>
        <stop offset="1" stop-color="var(--play-bottom)"/>
      </linearGradient>
      <linearGradient id="register-fill" x1="0" y1="0" x2="0" y2="1">
        <stop offset="0" stop-color="var(--register-top)"/>
        <stop offset="1" stop-color="var(--register-bottom)"/>
      </linearGradient>
    </defs>

    <path class="card-edge" fill="url(#card-edge-fill)"
      d="M345 176 L852 226 Q887 232 884 254 L852 430 Q848 452 820 451 L380 442 Q330 440 326 398 Z"/>
    <path class="card-face" fill="url(#card-fill)"
      d="M336 170 L845 213 Q878 219 876 242 L847 424 Q844 446 816 446 L380 434 Q322 432 320 390 L311 194 Q310 168 336 170 Z"/>

    <path class="button-play-shadow" fill="var(--button-shadow)" opacity="0.7"
      d="M484 434 Q483 428 490 427 L630 424 Q637 424 636 432 L633 468 Q632 476 624 476 L492 476 Q485 476 485 469 Z"/>
    <path class="button-play" fill="url(#play-fill)" stroke="var(--play-stroke)" stroke-width="1"
      d="M480 429 Q479 423 486 423 L624 419 Q632 419 631 427 L628 462 Q627 470 619 470 L488 470 Q481 470 481 463 Z"/>

    <path class="button-register-shadow" fill="var(--button-shadow)" opacity="0.7"
      d="M642 428 Q641 422 648 423 L787 432 Q794 433 794 440 L794 470 Q794 477 787 477 L655 476 Q647 476 646 469 Z"/>
    <path class="button-register" fill="url(#register-fill)" stroke="var(--register-stroke)" stroke-width="1"
      d="M638 424 Q637 418 644 419 L783 428 Q790 429 790 436 L790 464 Q790 471 783 471 L651 470 Q643 470 642 463 Z"/>
  </svg>

  <p class="field field-user">User ID</p>
  <p class="field field-password">***********</p>

  <p class="button-label button-label-play">play</p>
  <p class="button-label button-label-register">register</p>
</main>
</body>
</html>
```